Homeowners Marketing Leads website design

I need a new website designed using the our attached company logo. We sale New Movers lists to businesses that need to sale/market their services/products to homeowners, they use our list to call or mail those customers about doing business with them.
Our 3 Steps process is;
1. (Our Clients) Receive leads of the most recent New Movers in their area.
2. (Our Clients) Do direct marketing of their company's services/products to those New Movers.
3. If (Our Clients) feel these leads/lists are not fresh and accurate, then (Our Clients) have no obligation to pay us. The leads are FREE.

These are examples of the types of companies that would look for our website to be able get leads/list from us through our website;
-Carpeting/Flooring
-Residential Landscaping
-Heat/Air Conditioning Services
-Painting
-Home Remodeling
-Windows Replacement
-Plumbing
-Pest Control
-Home Security Systems
-Appliances
-Furniture
-Home Theater/TV Mounting
-Mattress
Etc.

Target Market(s)

We sell lead lists to companies looking to do a mailing or cold-calling campaign to Residential New Movers (Homeowners)

Number of Pages Required

2 page

Requirements
Must have
• Contact Form so that our clients can enter the following;
• Name
• (Their) Business Name
• Email to Receive Lead
• Industry (This input will be a drop-down on the form)
• Comments/Questions (Box)
• (Submit Button)

```html
<!DOCTYPE html>
<html lang="en">
<head>
<meta charset="utf-8">
<title>Homeward Leads</title>
<link href="https://fonts.googleapis.com/css2?family=Open+Sans:wdth,wght@75..100,400..700&display=swap" rel="stylesheet">
<style>
:root{
  --orange:#ff7a1a;
  --ink:#222;
  --body:#555;
  --nav:#545454;
  --panel:#555555;
  --light:#f2f2f2;
  --footer:#151515;
  --footer-base:#0a0a0a;
  --white:#fff;
}
*{box-sizing:border-box;margin:0;padding:0}
html,body{width:1200px;height:2375px;overflow:hidden;background:var(--white)}
body{font-family:"Open Sans",Arial,sans-serif;color:var(--body);position:relative}
.abs{position:absolute}
/* header */
.brand{left:98px;top:30px;display:flex;align-items:center;gap:12px}
.brand-mark{width:26px;height:26px;background:var(--orange)}
.brand-name{font-size:28px;font-weight:600;color:var(--orange)}
.contact-top{top:41px;font-size:14.5px;color:#333;display:flex;align-items:center;gap:10px;white-space:nowrap}
.contact-top svg{width:15px;height:15px;flex:none}
.contact-email{right:262px}
.contact-phone{right:100px}
.divider-v{left:961px;top:32px;width:1px;height:40px;background:#ddd}
/* hero */
.hero{left:0;top:130px;width:1200px;height:551px;background:linear-gradient(180deg,#8c8a7a 0%,#7b7c5e 35%,#5f8d36 62%,#6fa93a 100%)}
.nav{left:98px;top:106px;width:1002px;height:52px;background:var(--nav);display:flex;align-items:center;z-index:2}
.nav a{color:var(--white);font-size:13px;text-decoration:none;padding:0 20px;position:relative;line-height:52px}
.nav a+a::before{content:"|";position:absolute;left:-3px;color:#ccc}
.nav a.active{background:var(--orange);width:102px;text-align:center;padding:0}
.nav a.active+a::before{content:none}
.nav .search{position:absolute;right:8px;top:11px;width:30px;height:30px;border-radius:50%;background:#3a3a3a;display:flex;align-items:center;justify-content:center}
.hero-caption{left:98px;top:361px;width:443px;height:166px;background:rgba(40,40,40,.72);padding:22px 10px 0 26px;color:var(--white)}
.hero-caption p{font-size:19.5px;line-height:1.5;white-space:nowrap;letter-spacing:-.2px}
.btn{display:inline-flex;align-items:center;gap:10px;font-size:12px;color:var(--white);padding:0 18px;height:36px}
.btn-dark{background:#5a5a5a;margin-top:22px}
.btn-orange{background:var(--orange)}
.btn svg{width:15px;height:15px}
.who{left:98px;top:622px;width:1002px;height:119px;background:var(--orange);text-align:center;color:var(--white);padding-top:26px}
.who h2{font-size:26px;font-weight:700;margin-bottom:8px}
.who p{font-size:14px;opacity:.95}
/* welcome */
.welcome-title{left:98px;top:797px;font-size:31px;font-weight:600;color:var(--ink)}
.welcome-photo{left:98px;top:877px;width:277px;height:192px;background:linear-gradient(180deg,#9cc7ec 0%,#c9d7e0 45%,#8fae6a 100%)}
.welcome-text{left:407px;top:870px;width:348px;font-size:11.5px;line-height:18px;font-stretch:85%;color:#777}
.welcome-text strong{color:#333;font-weight:600}
.welcome-more{left:98px;top:1094px;width:660px;font-size:12px;line-height:1.6;color:#777}
.welcome-btn{left:98px;top:1148px}
/* quick contact */
.quick{left:780px;top:806px;width:320px;height:399px;background:var(--panel);padding:20px 32px}
.quick h3{color:var(--white);font-size:23px;font-weight:600;text-align:center;margin-bottom:22px}
.field{height:38px;background:var(--white);margin-bottom:6px;font-size:12px;color:#999;padding:0 12px;display:flex;align-items:center;justify-content:space-between}
.field.message{height:70px;align-items:flex-start;padding-top:12px}
.submit{height:45px;background:var(--orange);color:var(--white);font-weight:700;font-size:15px;display:flex;align-items:center;justify-content:center;margin-top:10px}
/* services */
.services{left:0;top:1285px;width:1200px;height:395px;background:var(--light)}
.section-title{width:1200px;left:0;text-align:center;font-size:30px;font-weight:600}
.service{width:200px;text-align:center;top:1436px}
.service .icon{width:71px;height:71px;border:2px solid var(--orange);margin:0 auto 18px;display:flex;align-items:center;justify-content:center;background:var(--white)}
.service .icon.on{background:var(--orange)}
.service .icon svg{width:36px;height:36px}
.service p{font-size:15px;font-weight:600;color:#111;line-height:1.2}
.dots{left:576px;top:1624px;display:flex;gap:6px}
.dots i{width:6px;height:6px;background:#aaa;display:block}
.dots i:first-child{background:var(--orange)}
/* process */
.process{left:0;top:1680px;width:1200px;height:387px;background:var(--orange)}
.step-circle{width:130px;height:130px;border-radius:50%;background:var(--white);top:1801px;display:flex;align-items:center;justify-content:center;font-size:25px;color:#333}
.step-line{top:1866px;height:1px;background:rgba(255,255,255,.8)}
.step-text{top:1950px;width:290px;text-align:center;font-size:14px;font-weight:600;color:var(--white);line-height:1.55}
/* footer */
.footer{left:0;top:2067px;width:1200px;height:247px;background:var(--footer)}
.f-col{top:2104px;color:#eee;font-size:11.5px}
.f-col h4{font-size:12.5px;font-weight:600;margin-bottom:14px;letter-spacing:.2px}
.f-col p{line-height:1.45}
.f-col ul{list-style:none}
.f-col li{margin-bottom:6px;padding-left:20px;position:relative}
.f-col li::before{content:"";position:absolute;left:2px;top:6px;width:5px;height:5px;border-radius:50%;background:#eee}
.f-col .row{display:flex;align-items:center;gap:10px;margin-top:6px;white-space:nowrap}
.f-col .row svg{width:12px;height:12px;flex:none}
.more{left:262px;top:2237px;color:#eee;font-size:12px;display:flex;gap:8px;align-items:center}
.base{left:0;top:2314px;width:1200px;height:61px;background:var(--footer-base)}
.copy{left:98px;top:2336px;color:#ddd;font-size:11px}
.social{left:1000px;top:2335px;display:flex;gap:14px}
.social i{width:14px;height:14px;border-radius:50%;background:#eee;display:block}
</style>
</head>
<body>

<header>
  <div class="abs brand"><span class="brand-mark"></span><span class="brand-name">Homeward Leads</span></div>
  <div class="abs contact-top contact-email">
    <svg viewBox="0 0 16 16"><rect x="1" y="3" width="14" height="10" fill="#444"/><path d="M1 3l7 6 7-6" stroke="#fff" stroke-width="1.2" fill="none"/></svg>
    hello@homewardleads.example
  </div>
  <div class="abs divider-v"></div>
  <div class="abs contact-top contact-phone">
    <svg viewBox="0 0 16 16"><path d="M3 1l3 1 1 4-2 1c1 2 2 3 4 4l1-2 4 1 1 3-2 2C7 15 1 9 1 3z" fill="#444"/></svg>
    0400 555 218
  </div>
</header>

<div class="abs hero" role="img" aria-label="Photo of a stone house front with trimmed shrubs, a stone retaining wall and green lawn"></div>

<nav class="abs nav">
  <a class="active">HOME</a><a>ABOUT US</a><a>SERVICES</a><a>GALLERY</a><a>TESTIMONIALS</a><a>POLICIES</a><a>FAQ'S</a><a>CONTACT US</a>
  <span class="search"><svg width="13" height="13" viewBox="0 0 14 14"><circle cx="6" cy="6" r="4" stroke="#fff" stroke-width="1.6" fill="none"/><path d="M9 9l4 4" stroke="#fff" stroke-width="1.8"/></svg></span>
</nav>

<div class="abs hero-caption">
  <p>Lorem ipsum dolor sit amet, consectetur<br>adipiscing elit. Vestibulum elit libero</p>
  <span class="btn btn-dark">Read More <svg viewBox="0 0 16 16"><circle cx="8" cy="8" r="7.5" fill="#fff"/><path d="M7 4.5l3.5 3.5L7 11.5" stroke="#5a5a5a" stroke-width="1.8" fill="none"/></svg></span>
</div>

<section class="abs who">
  <h2>Who We Are?</h2>
  <p>We are marketing company who does marketing of products such as appliances, plumbing , etc to new movers to an area</p>
</section>

<h1 class="abs welcome-title">WELCOME TO OUR SITE</h1>
<div class="abs welcome-photo" role="img" aria-label="Photo of a couple seen from behind looking at a new house"></div>
<p class="abs welcome-text"><strong>Established in 1991, Harbourline Builders is a building company that prides itself on quality control. It is the attention to detail in all aspects of the building and construction process, from initial client contact, through to handover and beyond, that sets us apart from other builders.</strong>As a smaller builder, our focus on quality construction, attention to detail, and scheduled timeframe, from design to completion are paramount, and cannot be matched by our competitors or emphasised enough. We are a flexible building company that can design and build to suit any block of land, and any budget to suit our valued client's needs. Our goal is to achieve happy</p>
<p class="abs welcome-more">Our focus areas for building are Sydney South West, and North West precedents. We can also offer our services North, South, and beyond these boundaries of Sydney.</p>
<span class="abs btn btn-orange welcome-btn">View Our Services <svg viewBox="0 0 16 16"><circle cx="8" cy="8" r="7.5" fill="#fff"/><path d="M7 4.5l3.5 3.5L7 11.5" stroke="#ff7a1a" stroke-width="1.8" fill="none"/></svg></span>

<aside class="abs quick">
  <h3>QUICK CONTACT</h3>
  <div class="field">Name</div>
  <div class="field">Business Name</div>
  <div class="field">Email</div>
  <div class="field">Industry <svg width="12" height="8" viewBox="0 0 12 8"><path d="M1 1l5 5 5-5" stroke="#888" stroke-width="1.5" fill="none"/></svg></div>
  <div class="field message">Message</div>
  <div class="submit">SUBMIT</div>
</aside>

<section class="abs services"></section>
<h2 class="abs section-title" style="top:1333px;color:#222">OUR SERVICES</h2>

<div class="abs service" style="left:85px">
  <div class="icon on"><svg viewBox="0 0 36 36"><path d="M18 8l14 10-14 10L4 18z" fill="#fff"/><path d="M11 13l14 10M18 8l-7 5M25 13l-14 10" stroke="#ff7a1a" stroke-width="1.5"/></svg></div>
  <p>CARPETING/FLOORING</p>
</div>
<div class="abs service" style="left:291px">
  <div class="icon"><svg viewBox="0 0 36 36"><path d="M18 6L4 18h4v12h8v-7h4v7h8V18h4z" fill="#111"/></svg></div>
  <p>RESIDENTIAL<br>LANDSCAPING</p>
</div>
<div class="abs service" style="left:497px">
  <div class="icon"><svg viewBox="0 0 36 36"><rect x="4" y="9" width="28" height="12" fill="none" stroke="#111" stroke-width="2"/><path d="M7 14h22M7 17h22M10 24v5M16 24v5M22 24v5" stroke="#111" stroke-width="1.6"/></svg></div>
  <p>HEAT/AIR CONDITIONING<br>SERVICES</p>
</div>
<div class="abs service" style="left:695px">
  <div class="icon"><svg viewBox="0 0 36 36"><path d="M24 5l7 7-9 9-7-7z" fill="#111"/><path d="M15 16l5 5-9 9-4-1-1-4z" fill="none" stroke="#111" stroke-width="2"/></svg></div>
  <p>PAINTING</p>
</div>
<div class="abs service" style="left:881px">
  <div class="icon"><svg viewBox="0 0 36 36"><path d="M18 5L5 16v15h26V16z" fill="#111"/><rect x="12" y="19" width="8" height="12" fill="#fff"/><path d="M22 20h6v5h-6z" fill="#fff"/></svg></div>
  <p>HOME REMODELING</p>
</div>
<div class="abs dots"><i></i><i></i><i></i><i></i></div>

<section class="abs process"></section>
<h2 class="abs section-title" style="top:1710px;color:#fff">OUR PROCESS</h2>
<div class="abs step-line" style="left:320px;width:217px"></div>
<div class="abs step-line" style="left:667px;width:211px"></div>
<svg class="abs" style="left:414px;top:1851px" width="18" height="30" viewBox="0 0 18 30"><path d="M2 1l14 14L2 29" stroke="#fff" stroke-width="1.2" fill="none"/></svg>
<svg class="abs" style="left:755px;top:1851px" width="18" height="30" viewBox="0 0 18 30"><path d="M2 1l14 14L2 29" stroke="#fff" stroke-width="1.2" fill="none"/></svg>
<div class="abs step-circle" style="left:190px">01</div>
<div class="abs step-circle" style="left:537px">02</div>
<div class="abs step-circle" style="left:878px">03</div>
<p class="abs step-text" style="left:110px">Receive leads of the most recent New Movers in their area.</p>
<p class="abs step-text" style="left:457px">Do direct marketing of their company's services/products to those New Movers.</p>
<p class="abs step-text" style="left:798px">If feel these leads/lists are not fresh and accurate, then (Our Clients) have no obligation to pay us. The leads are FREE.</p>

<footer>
  <div class="abs footer"></div>
  <div class="abs f-col" style="left:101px;width:225px">
    <h4>WHO WE ARE</h4>
    <p>Lorem ipsum dolor sit amet, consectetur adipiscing elit. Nullam venenatis velit blandit est condimentum aliquet. Curabitur ut libero justo. Nulla ut ex facilisis, tincidunt quam vitae, iaculis orci. Nullam eu faucibus nibh.</p>
  </div>
  <div class="abs more">More <svg width="14" height="14" viewBox="0 0 16 16"><circle cx="8" cy="8" r="7" stroke="#eee" stroke-width="1.3" fill="none"/><path d="M7 5l3 3-3 3" stroke="#eee" stroke-width="1.5" fill="none"/></svg></div>
  <div class="abs f-col" style="left:445px">
    <h4>USEFUL LINKS</h4>
    <ul><li>Terms &amp; Conditions</li><li>Privacy Policy</li><li>Service</li><li>FAQ</li><li>Sitemap</li><li>Contact Us</li></ul>
  </div>
  <div class="abs f-col" style="left:657px">
    <h4>MORE LINKS</h4>
    <ul><li>Home</li><li>About Us</li><li>Service</li><li>Testimonials</li><li>Gallery</li><li>Contact Us</li></ul>
  </div>
  <div class="abs f-col" style="left:885px;width:230px">
    <h4>GET IN TOUCH</h4>
    <p>Doloreiur quia commolu ptatemp dolupta oreprerum tibusam eumenis et consent accullignis dentibea</p>
    <div class="row"><svg viewBox="0 0 12 12"><path d="M6 0a4 4 0 0 1 4 4c0 3-4 8-4 8S2 7 2 4a4 4 0 0 1 4-4z" fill="#eee"/><circle cx="6" cy="4" r="1.5" fill="#151515"/></svg>PO Box 42 Maple Grove 2190</div>
    <div class="row"><svg viewBox="0 0 16 16"><path d="M3 1l3 1 1 4-2 1c1 2 2 3 4 4l1-2 4 1 1 3-2 2C7 15 1 9 1 3z" fill="#eee"/></svg>0400 555 218</div>
    <div class="row"><svg viewBox="0 0 16 16"><rect x="1" y="3" width="14" height="10" fill="#eee"/><path d="M1 3l7 6 7-6" stroke="#151515" stroke-width="1.2" fill="none"/></svg>hello@homewardleads.example</div>
  </div>
  <div class="abs base"></div>
  <p class="abs copy">© 2016 homewardleads. All rights reserved.</p>
  <div class="abs social"><i></i><i></i><i></i><i></i></div>
</footer>

</body>
</html>
```